October Billboard TX

Billboard - creative design using company colors. Previous billboard graphic is included for reference along with a rough example of the requested "less busy" design. Required graphics for the simple billboard design are also included in the upload. Billboard dimensions are attached. Need this design ASAP!

```html
<!DOCTYPE html>
<html lang="en">
<head>
<meta charset="utf-8">
<title>Little Lens Vision Billboard</title>
<link rel="stylesheet" href="https://fonts.googleapis.com/css2?family=Poppins:wght@600;700;800&family=Roboto+Condensed:ital,wght@1,700&display=swap">
<style>
  :root {
    --stage: #6a6a6a;
    --paper: #ffffff;
    --brand-blue: #1170b9;
    --brand-navy: #0c4f87;
    --brand-red: #e30613;
    --brand-yellow: #ffe600;
    --ink: #333333;
  }
  * { box-sizing: border-box; margin: 0; padding: 0; }
  html, body {
    width: 860px; height: 1200px; overflow: hidden;
    background: var(--stage);
    font-family: "Poppins", sans-serif;
  }
  .billboard {
    position: absolute; left: 30px; top: 400px;
    width: 800px; height: 399px;
    background: var(--paper);
    overflow: hidden;
    box-shadow: 10px 14px 22px rgba(0,0,0,.45);
  }
  .billboard-shapes { position: absolute; inset: 0; }

  .brand {
    position: absolute; left: 30px; top: 44px;
    display: flex; align-items: center; gap: 10px;
    color: var(--brand-blue);
    font-weight: 700; font-size: 22px; line-height: 1.1;
  }
  .brand-dot {
    width: 34px; height: 34px; border-radius: 50%;
    background: var(--brand-blue); flex: none;
  }

  .age-list { position: absolute; left: 0; top: 147px; list-style: none; }
  .age-list li {
    width: 227px; height: 27px; margin-bottom: 3px;
    border-radius: 0 14px 14px 0;
    background: var(--brand-blue);
    color: #fff; font-weight: 600; font-size: 16px;
    display: flex; align-items: center; padding-left: 31px; gap: 5px;
  }
  .age-list li:nth-child(even) { background: var(--brand-navy); }
  .tick { width: 13px; height: 13px; flex: none; }

  .quote-frame {
    position: absolute; left: 272px; top: 54px;
    width: 248px; height: 238px;
    border-left: 1.5px solid var(--brand-blue);
    border-top: 1.5px solid var(--brand-blue);
    border-top-left-radius: 10px;
  }
  .quote-mark {
    position: absolute; left: 291px; top: 38px;
    padding: 0 4px; background: var(--paper);
    color: var(--brand-blue);
    font-family: "Poppins", sans-serif; font-weight: 800;
    font-size: 54px; line-height: 1;
  }
  .quote-text {
    position: absolute; left: 295px; top: 86px;
    font-family: "Roboto Condensed", sans-serif; font-style: italic; font-weight: 700;
    font-size: 22px; line-height: 24.7px; color: var(--ink);
  }
  .quote-author {
    position: absolute; left: 295px; top: 241px;
    font-weight: 700; font-style: italic; font-size: 15px;
    color: var(--brand-blue);
  }

  .call-label {
    position: absolute; left: 26px; top: 306px;
    font-weight: 800; font-size: 23px; line-height: 1; color: #fff;
    letter-spacing: -0.2px;
  }
  .call-label span { color: var(--brand-yellow); }
  .call-number {
    position: absolute; left: 26px; top: 334px;
    display: flex; align-items: center; gap: 8px;
    color: #fff; font-weight: 800; font-size: 42px; line-height: 1;
    letter-spacing: -0.5px;
  }
  .phone-icon { width: 40px; height: 40px; flex: none; }

  .kids-badge {
    position: absolute; left: 413px; top: 248px;
    width: 124px; height: 124px; border-radius: 50%;
    background: var(--brand-red);
    display: flex; align-items: center; justify-content: center;
    box-shadow: 0 4px 8px rgba(0,0,0,.3);
  }
  .kids-badge-inner {
    width: 104px; height: 104px; border-radius: 50%;
    background: var(--brand-yellow);
    display: flex; flex-direction: column; align-items: center; justify-content: center;
    font-weight: 800; font-size: 27px; line-height: .95; letter-spacing: -1px;
  }
  .kids-badge-inner .kids { color: var(--brand-red); }
  .kids-badge-inner .only { color: var(--brand-navy); }

  .spanish-pill {
    position: absolute; left: 548px; top: 337px;
    width: 226px; height: 34px; border-radius: 17px;
    background: var(--brand-blue); border: 1.5px solid #fff;
    display: flex; align-items: center; justify-content: center; gap: 4px;
    color: #fff; font-weight: 700; font-size: 14px; letter-spacing: -0.2px;
  }
  .spanish-pill span { color: var(--brand-yellow); }
</style>
</head>
<body>
<main class="billboard">
  <svg class="billboard-shapes" viewBox="0 0 800 399" width="800" height="399">
    <defs>
      <linearGradient id="photoTone" x1="0" y1="0" x2="1" y2="1">
        <stop offset="0" stop-color="#3a2a24"/>
        <stop offset="0.45" stop-color="#e3b9a0"/>
        <stop offset="1" stop-color="#f4e25a"/>
      </linearGradient>
    </defs>
    <path role="img" aria-label="Photo of a smiling mother hugging her young daughter who wears red glasses"
          d="M560,40 C600,20 720,22 800,34 L800,240 L520,300 C520,220 520,90 560,40 Z"
          fill="url(#photoTone)"/>
    <path class="wave-blue" fill="var(--brand-blue)"
          d="M0,258 C200,276 380,292 480,292 C620,290 720,250 800,208 L800,234 C720,270 620,300 480,300 C380,300 200,282 0,264 Z"/>
    <path class="wave-red" fill="var(--brand-red)"
          d="M0,264 C200,282 380,300 480,300 C620,300 720,270 800,234 L800,399 L0,399 Z"/>
  </svg>

  <div class="brand">
    <div class="brand-dot"></div>
    <div>Little Lens Vision<br>of El Paso</div>
  </div>

  <ul class="age-list">
    <li><svg class="tick" viewBox="0 0 14 14"><circle cx="7" cy="7" r="7" fill="#ffe600"/><path d="M3.8,7.2 L6,9.3 L10.2,4.9" fill="none" stroke="#0c4f87" stroke-width="1.8"/></svg>Newborns</li>
    <li><svg class="tick" viewBox="0 0 14 14"><circle cx="7" cy="7" r="7" fill="#ffe600"/><path d="M3.8,7.2 L6,9.3 L10.2,4.9" fill="none" stroke="#0c4f87" stroke-width="1.8"/></svg>Infants</li>
    <li><svg class="tick" viewBox="0 0 14 14"><circle cx="7" cy="7" r="7" fill="#ffe600"/><path d="M3.8,7.2 L6,9.3 L10.2,4.9" fill="none" stroke="#0c4f87" stroke-width="1.8"/></svg>Toddlers</li>
    <li><svg class="tick" viewBox="0 0 14 14"><circle cx="7" cy="7" r="7" fill="#ffe600"/><path d="M3.8,7.2 L6,9.3 L10.2,4.9" fill="none" stroke="#0c4f87" stroke-width="1.8"/></svg>Tweens &amp; Teens</li>
  </ul>

  <div class="quote-frame"></div>
  <div class="quote-mark">“</div>
  <p class="quote-text">I take my child<br>to el paso's<br>most qualified<br>and experienced<br>pediatric<br>eye doctor</p>
  <p class="quote-author">M. Reyes</p>

  <p class="call-label">FOR <span>APPOINTMENTS CALL</span></p>
  <p class="call-number">
    <svg class="phone-icon" viewBox="0 0 40 40"><circle cx="20" cy="20" r="20" fill="#ffe600"/><path d="M13,11 L17,10 L19,16 L16.5,18 C18,21.5 19,22.5 22,23.5 L24,21 L30,23 L29,27 C28,29 25,30 22,29 C17,27 13,23 11,18 C10,15 11,12 13,11 Z" fill="#e30613"/></svg>
    (915) 555-0142
  </p>

  <div class="kids-badge">
    <div class="kids-badge-inner"><span class="kids">KIDS</span><span class="only">ONLY</span></div>
  </div>

  <p class="spanish-pill">La Doctora <span>Habla Español</span></p>
</main>
</body>
</html>
```